Design for Chirpwall Ad to promote Laptops purchase

Need a graphic design for a Chirpwall Ad - to promote 2 laptops (PC and Zorvane) with the stated required ad-text.

AD TEXT:

FOR SME BUSINESS ONLY!
Chat with us!
To get advice on how to apply
and defray up to 80%* of business laptop purchase cost!

*Terms and Conditions apply

Image for reference only

Target Market(s)

Small medium business

Font styles to use
Sans Serif

Requirements
Must have
• 2 laptop images (see attached ) - 1 vector image of ZORVANE , and pls try to create another vector image of PC laptop (where screen is showing Blue Pendrel screen)

```html
<!DOCTYPE html>
<html lang="en">
<head>
<meta charset="utf-8">
<title>Chirpwall Ad – Business Laptops for SMEs</title>
<link rel="stylesheet" href="https://fonts.googleapis.com/css2?family=Fredoka:wght@500;600&family=Barlow+Semi+Condensed:wght@500;600&display=swap">
<style>
  :root {
    --bg-deep: #3f1f4b;
    --band-purple: #6a3c80;
    --band-violet: #8a5aa3;
    --glow-lilac: #c7a6d8;
    --glow-cyan: #a9d9ea;
    --ink: #2b0d3b;
    --note: #f1e8f6;
    --screen-pc: #1f8fe0;
    --screen-pc-light: #35b8f0;
    --screen-z: #0d1b33;
    --screen-z-light: #2d4a78;
    --body-silver: #c9c9cc;
    --bezel: #1b1b1e;
  }
  html, body {
    margin: 0;
    padding: 0;
    width: 1200px;
    height: 1000px;
    overflow: hidden;
  }
  .ad {
    position: relative;
    width: 1200px;
    height: 1000px;
    background: var(--bg-deep);
    overflow: hidden;
    font-family: "Fredoka", sans-serif;
    color: var(--ink);
  }
  .ad__band {
    position: absolute;
    left: 0;
    top: 185px;
    width: 1200px;
    height: 630px;
    background:
      radial-gradient(ellipse 170px 330px at 600px 330px, var(--glow-cyan) 0%, rgba(169,217,234,0.5) 45%, rgba(169,217,234,0) 100%),
      radial-gradient(ellipse 360px 380px at 600px 300px, var(--glow-lilac) 0%, rgba(199,166,216,0.35) 55%, rgba(199,166,216,0) 100%),
      radial-gradient(ellipse 700px 300px at 600px 315px, var(--band-violet) 0%, var(--band-purple) 60%, rgba(106,60,128,0) 100%);
    filter: blur(6px);
  }
  .ad__copy {
    position: absolute;
    left: 0;
    width: 1200px;
    text-align: center;
    margin: 0;
  }
  .ad__eyebrow {
    top: 240px;
    font-family: "Barlow Semi Condensed", sans-serif;
    font-weight: 600;
    font-size: 40px;
    letter-spacing: 5px;
  }
  .ad__headline {
    top: 318px;
    font-weight: 600;
    font-size: 90px;
    line-height: 1;
    letter-spacing: 7px;
  }
  .ad__subline {
    top: 452px;
    font-weight: 500;
    font-size: 29px;
    line-height: 36px;
    letter-spacing: 2.5px;
  }
  .laptop {
    position: absolute;
    border-radius: 10px 10px 6px 6px;
  }
  .laptop--pc {
    left: 62px;
    top: 548px;
    width: 372px;
    height: 220px;
    background:
      linear-gradient(180deg, rgba(0,0,0,0) 88%, var(--body-silver) 88%),
      linear-gradient(155deg, var(--screen-pc-light) 0%, var(--screen-pc) 45%, var(--bezel) 80%);
  }
  .laptop--zorvane {
    left: 748px;
    top: 560px;
    width: 386px;
    height: 208px;
    background:
      linear-gradient(180deg, rgba(0,0,0,0) 88%, var(--body-silver) 88%),
      linear-gradient(200deg, var(--screen-z-light) 0%, var(--screen-z) 50%, var(--bezel) 85%);
  }
  .ad__terms {
    position: absolute;
    left: 30px;
    top: 786px;
    margin: 0;
    font-family: "Barlow Semi Condensed", sans-serif;
    font-weight: 500;
    font-size: 14px;
    letter-spacing: 1px;
    color: var(--note);
  }
</style>
</head>
<body>
  <main class="ad">
    <div class="ad__band" aria-hidden="true"></div>

    <p class="ad__copy ad__eyebrow">FOR SME BUSINESS ONLY!</p>
    <h1 class="ad__copy ad__headline">Chat with us!</h1>
    <p class="ad__copy ad__subline">To get advice on how to apply<br>and defray up to 80%* of business laptop purchase cost!</p>

    <div class="laptop laptop--pc" role="img" aria-label="PC laptop illustration with a blue Pendrel desktop screen"></div>
    <div class="laptop laptop--zorvane" role="img" aria-label="Zorvane laptop illustration with a galaxy wallpaper screen"></div>

    <p class="ad__terms">*Terms and Conditions apply</p>
  </main>
</body>
</html>
```